KORBALT

The business want a professional looking business card. We have a scetch we will add but want the extra upgrade, and would like more suggestions for variations of our business cards.

```html
<!DOCTYPE html>
<html lang="en">
<head>
<meta charset="utf-8">
<title>KORBALT – Business Card Variations</title>
<link href="https://fonts.googleapis.com/css2?family=Cormorant+Garamond:wght@500;600&family=Montserrat:wght@400;500&display=swap" rel="stylesheet">
<style>
  :root {
    --canvas: #939497;
    --black: #000000;
    --cream: #fdf6ec;
    --brown: #3a261d;
    --gold: #c9a34e;
    --gold-light: #f0dca0;
    --gold-dark: #7a5a2e;
    --ink: #3a2a20;
    --white: #ffffff;
  }
  * { margin: 0; padding: 0; box-sizing: border-box; }
  html, body { width: 1200px; height: 1200px; overflow: hidden; background: var(--canvas); }
  .sheet { position: relative; width: 1200px; height: 1200px; }

  .card { position: absolute; width: 454px; height: 259px; overflow: hidden; box-shadow: 1px 1px 2px rgba(0,0,0,.35); }
  .col-left { left: 124px; }
  .col-right { left: 623px; }
  .row-1 { top: 163px; }
  .row-2 { top: 465px; }
  .row-3 { top: 777px; }

  .card--black { background: var(--black); }
  .card--cream { background: var(--cream); }
  .card--brown { background: var(--brown); }

  .firm { position: absolute; left: 31px; font-family: "Cormorant Garamond", serif; font-weight: 500; font-size: 26px; letter-spacing: -0.3px; line-height: 1; white-space: nowrap; }
  .person { position: absolute; left: 31px; font-family: "Montserrat", sans-serif; font-weight: 500; font-size: 19px; line-height: 1; white-space: nowrap; }
  .role { position: absolute; left: 31px; font-family: "Montserrat", sans-serif; font-weight: 400; font-size: 14px; line-height: 1; }
  .contact { position: absolute; left: 31px; display: flex; align-items: center; gap: 9px; font-family: "Montserrat", sans-serif; font-size: 14.5px; line-height: 1; }
  .contact svg { width: 18px; height: 18px; flex: none; }

  .on-dark .firm { color: var(--gold); }
  .on-dark .person, .on-dark .role, .on-dark .contact { color: var(--white); }
  .on-light .firm, .on-light .person, .on-light .role, .on-light .contact { color: var(--ink); }

  .icon { fill: none; stroke: var(--gold); stroke-width: 1.3; }

  .divider-v { position: absolute; width: 1px; background: var(--gold); }
  .divider-h { position: absolute; height: 1px; background: linear-gradient(90deg, var(--gold-dark), var(--gold), var(--gold-light)); }

  .gold-band { position: absolute; left: 0; right: 0; bottom: 0; height: 16px; background: linear-gradient(90deg, #efdfa6 0%, #fcd97a 18%, #b38c48 45%, #7a5a2e 60%, #b38c48 80%, #e2c48a 100%); }

  .brand-mark { position: absolute; display: flex; flex-direction: column; align-items: center; gap: 8px; transform: translate(-50%, -50%); }
  .brand-mark .dot { width: 18px; height: 18px; border-radius: 50%; background: var(--gold); }
  .brand-mark .word { font-family: "Cormorant Garamond", serif; font-weight: 600; color: var(--gold); letter-spacing: 4px; line-height: 1; }

  .frame { position: absolute; inset: 16px; border: 1px solid var(--gold); }

  .panel-brown { position: absolute; left: 291px; top: 0; width: 163px; height: 100%; background: linear-gradient(160deg, #3d281e, #362319); }

  .lockup { position: absolute; left: 81px; top: 128px; display: flex; align-items: center; transform: translateY(-50%); }
  .lockup .dot { width: 22px; height: 22px; border-radius: 50%; background: var(--gold); margin-left: -11px; }
  .lockup-word { position: absolute; left: 165px; top: 131px; transform: translateY(-50%); font-family: "Cormorant Garamond", serif; font-weight: 600; font-size: 42px; letter-spacing: 9px; color: var(--gold); line-height: 1; }
</style>
</head>
<body>
<main class="sheet">

  <!-- Front, black -->
  <section class="card card--black col-left row-1 on-dark">
    <p class="firm" style="top:42px">KORBALT VESTHEIM</p>
    <p class="person" style="top:84px">Lars Erik Vestheim</p>
    <p class="role" style="top:105px">CEO &amp; Founder</p>
    <p class="contact" style="top:146px"><svg viewBox="0 0 18 18"><rect class="icon" x="5" y="1.5" width="8" height="15" rx="1.2"/></svg>004791234567</p>
    <p class="contact" style="top:175px"><svg viewBox="0 0 18 18"><rect class="icon" x="1.5" y="4" width="15" height="10"/><path class="icon" d="M1.5 4l7.5 6 7.5-6M1.5 14l5.5-5M16.5 14l-5.5-5"/></svg>hello@korbalt.llc</p>
    <p class="contact" style="top:204px"><svg viewBox="0 0 18 18"><circle class="icon" cx="9" cy="9" r="7.5"/><ellipse class="icon" cx="9" cy="9" rx="3.2" ry="7.5"/><path class="icon" d="M1.5 9h15M3 5h12M3 13h12"/></svg>www.korbalt.llc</p>
    <div class="divider-v" style="left:299px; top:31px; height:197px"></div>
    <div class="brand-mark" style="left:379px; top:130px"><span class="dot"></span><span class="word" style="font-size:20px">KORBALT</span></div>
  </section>

  <!-- Back, black -->
  <section class="card card--black col-right row-1">
    <div class="frame"></div>
    <div class="brand-mark" style="left:227px; top:130px; gap:22px"><span class="dot" style="width:30px;height:30px"></span><span class="word" style="font-size:40px; letter-spacing:10px">KORBALT</span></div>
  </section>

  <!-- Front, cream with gold band -->
  <section class="card card--cream col-left row-2 on-light">
    <p class="firm" style="top:32px">KORBALT VESTHEIM</p>
    <p class="person" style="top:64px">Lars Erik Vestheim</p>
    <p class="role" style="top:85px">CEO &amp; Founder</p>
    <div class="brand-mark" style="left:381px; top:64px"><span class="dot"></span><span class="word" style="font-size:18px">KORBALT</span></div>
    <div class="divider-h" style="left:31px; top:117px; width:390px"></div>
    <p class="contact" style="top:136px"><svg viewBox="0 0 18 18"><rect class="icon" x="5" y="1.5" width="8" height="15" rx="1.2"/></svg>004791234567</p>
    <p class="contact" style="top:165px"><svg viewBox="0 0 18 18"><rect class="icon" x="1.5" y="4" width="15" height="10"/><path class="icon" d="M1.5 4l7.5 6 7.5-6M1.5 14l5.5-5M16.5 14l-5.5-5"/></svg>hello@korbalt.llc</p>
    <p class="contact" style="top:194px"><svg viewBox="0 0 18 18"><circle class="icon" cx="9" cy="9" r="7.5"/><ellipse class="icon" cx="9" cy="9" rx="3.2" ry="7.5"/><path class="icon" d="M1.5 9h15M3 5h12M3 13h12"/></svg>www.korbalt.llc</p>
    <div class="gold-band"></div>
  </section>

  <!-- Back, cream -->
  <section class="card card--cream col-right row-2">
    <div class="frame"></div>
    <div class="brand-mark" style="left:227px; top:130px; gap:22px"><span class="dot" style="width:30px;height:30px"></span><span class="word" style="font-size:40px; letter-spacing:10px">KORBALT</span></div>
  </section>

  <!-- Front, cream and brown split -->
  <section class="card card--cream col-left row-3 on-light">
    <p class="firm" style="top:40px">KORBALT VESTHEIM</p>
    <p class="person" style="top:72px">Lars Erik Vestheim</p>
    <p class="role" style="top:94px">CEO &amp; Founder</p>
    <p class="contact" style="top:143px"><svg viewBox="0 0 18 18"><rect class="icon" x="5" y="1.5" width="8" height="15" rx="1.2"/></svg>004791234567</p>
    <p class="contact" style="top:172px"><svg viewBox="0 0 18 18"><rect class="icon" x="1.5" y="4" width="15" height="10"/><path class="icon" d="M1.5 4l7.5 6 7.5-6M1.5 14l5.5-5M16.5 14l-5.5-5"/></svg>hello@korbalt.llc</p>
    <p class="contact" style="top:201px"><svg viewBox="0 0 18 18"><circle class="icon" cx="9" cy="9" r="7.5"/><ellipse class="icon" cx="9" cy="9" rx="3.2" ry="7.5"/><path class="icon" d="M1.5 9h15M3 5h12M3 13h12"/></svg>www.korbalt.llc</p>
    <div class="panel-brown"></div>
  </section>

  <!-- Back, brown -->
  <section class="card card--brown col-right row-3">
    <div class="lockup"><span class="dot"></span></div>
    <div class="divider-v" style="left:145px; top:71px; height:107px"></div>
    <p class="lockup-word">KORBALT</p>
  </section>

</main>
</body>
</html>
```